DALMO-FIX
Business Card, Stationary, Envelope & Invoice Design
Hi Designers, just uploaded a png file, colors in blue, can we try that???
Thanks
Hi Designers, We would like to have a folder desing also.

```html
<!DOCTYPE html>
<html lang="en">
<head>
<meta charset="utf-8">
<title>DALMO-FIX Stationery Set</title>
<link href="https://fonts.googleapis.com/css2?family=Montserrat:wght@400;700&display=swap" rel="stylesheet">
<style>
  :root {
    --backdrop: #3b3b3d;
    --paper: #fbfbfb;
    --ink: #2a2a2a;
    --muted: #8a8a8a;
    --amber: #e39224;
    --amber-deep: #6e3b0c;
    --charcoal: #161616;
    --label: #9a9a9a;
  }
  * { box-sizing: border-box; margin: 0; padding: 0; }
  html, body { width: 1200px; height: 312px; overflow: hidden; }
  body {
    background: var(--backdrop);
    font-family: "Montserrat", Arial, sans-serif;
    position: relative;
  }
  .piece { position: absolute; background: var(--paper); box-shadow: 0 2px 4px rgba(0,0,0,.45); overflow: hidden; }
  .amber-band { position: absolute; left: 0; right: 0; top: 0; background: linear-gradient(90deg, var(--amber-deep), var(--amber) 55%, var(--amber-deep)); }
  .brand { position: absolute; display: flex; align-items: center; gap: 3px; font-weight: 700; color: var(--ink); letter-spacing: .3px; }
  .brand-mark { width: 6px; height: 6px; background: var(--amber); }
  .brand.on-dark { color: var(--paper); }
  .fine { position: absolute; font-size: 3.5px; line-height: 5px; color: var(--muted); }
  .label { position: absolute; font-size: 5px; color: var(--label); text-align: center; }

  .card { width: 66px; height: 41px; }
  .card-dark { background: var(--charcoal); }
  .card-dark .amber-band { height: 4px; top: auto; bottom: 0; }

  .letterhead { width: 204px; height: 269px; }
  .letterhead .amber-band { height: 6px; }
  .letterhead .brand { left: 14px; top: 12px; font-size: 8px; }
  .letterhead .contact { right: 14px; top: 13px; text-align: right; }
  .letterhead .footer { left: 0; right: 0; bottom: 8px; text-align: center; }

  .envelope { width: 192px; height: 86px; }
  .envelope .amber-band { height: 5px; }
  .envelope .brand { left: 10px; top: 12px; font-size: 7px; }
  .envelope .return { left: 10px; top: 24px; }

  .envelope-back { left: 948px; width: 180px; }
</style>
</head>
<body>

  <!-- Business cards -->
  <div class="piece card" style="left:19px; top:127px;">
    <div class="brand" style="left:12px; top:16px; font-size:7px;"><span class="brand-mark"></span>DALMO-FIX</div>
  </div>
  <div class="piece card card-dark" style="left:89px; top:127px;">
    <div class="amber-band"></div>
    <div class="brand on-dark" style="left:8px; top:9px; font-size:6px;"><span class="brand-mark"></span>DALMO-FIX</div>
    <div class="fine" style="left:8px; top:22px; color:#ccc;">Alex Ward<br>Manager</div>
  </div>
  <div class="piece card" style="left:19px; top:180px;">
    <div class="brand" style="left:12px; top:16px; font-size:7px;"><span class="brand-mark"></span>DALMO-FIX</div>
  </div>
  <div class="piece card" style="left:89px; top:180px;">
    <div class="brand" style="left:7px; top:6px; font-size:5px;"><span class="brand-mark" style="width:4px;height:4px;"></span>DALMO-FIX</div>
    <div class="fine" style="left:7px; top:18px;">Tel 555 0100<br>info@dalmofix.com<br>12 Main St</div>
  </div>
  <div class="label" style="left:19px; top:226px; width:139px;">Business Cards</div>

  <!-- Letterheads -->
  <div class="piece letterhead" style="left:223px; top:19px;">
    <div class="amber-band"></div>
    <div class="brand"><span class="brand-mark"></span>DALMO-FIX</div>
    <div class="fine contact">12 Main St, Springfield<br>Tel 555 0100</div>
    <div class="fine footer">www.dalmofix.com</div>
  </div>
  <div class="label" style="left:223px; top:292px; width:204px;">Letterhead A</div>

  <div class="piece letterhead" style="left:444px; top:19px;">
    <div class="amber-band"></div>
    <div class="brand"><span class="brand-mark"></span>DALMO-FIX</div>
    <div class="fine contact">12 Main St, Springfield<br>Tel 555 0100</div>
    <div class="fine footer">www.dalmofix.com</div>
  </div>
  <div class="label" style="left:444px; top:292px; width:204px;">Letterhead B</div>

  <!-- Envelopes, front -->
  <div class="piece envelope" style="left:667px; top:24px;">
    <div class="amber-band"></div>
    <div class="brand"><span class="brand-mark"></span>DALMO-FIX</div>
    <div class="fine return">12 Main St</div>
  </div>
  <div class="label" style="left:667px; top:114px; width:192px;">Envelope A</div>

  <div class="piece envelope" style="left:667px; top:158px;">
    <div class="amber-band"></div>
    <div class="brand"><span class="brand-mark"></span>DALMO-FIX</div>
    <div class="fine return">12 Main St</div>
  </div>
  <div class="label" style="left:667px; top:248px; width:192px;">Envelope B</div>

  <!-- Envelopes, back with flaps -->
  <svg class="envelope-back" style="position:absolute; top:19px; height:270px;" viewBox="0 0 180 270" aria-hidden="true">
    <defs>
      <linearGradient id="flap-amber" x1="0" y1="0" x2="0" y2="1">
        <stop offset="0" stop-color="#e39224"/>
        <stop offset="1" stop-color="#6e3b0c"/>
      </linearGradient>
    </defs>
    <path d="M0 10 Q0 0 10 0 H170 Q180 0 180 10 V60 Q90 90 0 60 Z" fill="url(#flap-amber)"/>
    <rect x="0" y="62" width="180" height="30" fill="#fbfbfb"/>
    <path d="M0 78 Q0 70 10 70 H170 Q180 70 180 78 V112 Q90 140 0 112 Z" fill="#161616"/>
    <rect x="0" y="118" width="180" height="100" fill="#fbfbfb"/>
    <path d="M0 118 L90 165 L180 118" fill="none" stroke="#d8d8d8" stroke-width="1"/>
    <rect x="0" y="222" width="180" height="46" fill="#f2f2f2"/>
  </svg>

</body>
</html>
```